Business Card Design

We are a trucking company that do a lot of business one on one with shippers. Our enthusiasm, honesty and hard work make us a great company to work with. We want to not only leave a lasting impression by the professionalism of our drivers but also give them something to remember us by for the future. I have a logo already designed that matches the same logo on the trucks. Its simple yet captures people to remember the name. We are expanding our coverage area by almost 700 miles and want to get our brand out there by having shippers call us to come back and conduct more business. I would like part of the logo itself raised but the shadowing not to give it a unique look and feel.
Industry/Entity Type
Trucking Company
Contact Information for Business Card
K&M Hauling LLC
Kurt & Melinda Ashcombe
402.618.2093 Kurt
402.551.4387 Melinda
kmhaulingllc@mailora.net

```html
<!DOCTYPE html>
<html lang="en">
<head>
<meta charset="utf-8">
<title>K&amp;M Hauling LLC — Business Card</title>
<link rel="stylesheet" href="https://fonts.googleapis.com/css2?family=Questrial&display=swap">
<style>
  :root {
    --backdrop: #6f6f6f;
    --card-dark: #2a2a2a;
    --card-white: #ffffff;
    --card-gray: #7c7c7c;
    --rule-gray: #b5b5b5;
    --rule-dark: #3a3a3a;
    --brand-ink: #5a5a5a;
    --text-light: #ffffff;
  }
  * { margin: 0; padding: 0; box-sizing: border-box; }
  html, body {
    width: 1200px; height: 1179px; overflow: hidden;
    background: var(--backdrop);
    font-family: "Questrial", "Century Gothic", sans-serif;
  }
  .canvas {
    width: 1200px; height: 1179px;
    display: flex; align-items: center; justify-content: center;
  }
  .business-card {
    position: relative;
    width: 1000px; height: 574px;
    background: var(--card-white);
    overflow: hidden;
    box-shadow: 0 10px 30px rgba(0,0,0,0.25);
  }
  .name-band {
    position: absolute; left: 0; top: 0; width: 100%; height: 164px;
    background: var(--card-dark);
    display: flex; flex-direction: column; align-items: center; justify-content: center;
    color: var(--text-light);
    font-size: 48px; line-height: 1.12; text-align: center;
  }
  .rule { position: absolute; left: 0; width: 100%; }
  .rule--gray-top { top: 164px; height: 10px; background: var(--rule-gray); }
  .rule--dark-top { top: 178px; height: 3px; background: var(--rule-dark); }
  .rule--dark-bottom { top: 398px; height: 3px; background: var(--rule-dark); }
  .rule--gray-bottom { top: 405px; height: 10px; background: var(--rule-gray); }
  .brand {
    position: absolute; left: 0; top: 181px; width: 100%; height: 217px;
    display: flex; align-items: center; justify-content: center; gap: 26px;
  }
  .brand-mark {
    width: 78px; height: 78px; border-radius: 50%;
    border: 5px solid var(--brand-ink);
  }
  .brand-name { color: var(--brand-ink); font-size: 50px; }
  .contact-band {
    position: absolute; left: 0; top: 415px; width: 100%; height: 159px;
    background: var(--card-gray);
    padding: 18px 0 0 62px;
    color: var(--text-light); font-size: 30px; line-height: 35px;
  }
  .contact-line { display: flex; align-items: center; gap: 12px; }
  .contact-icon { width: 20px; height: 24px; flex: none; }
</style>
</head>
<body>
<main class="canvas">
  <article class="business-card">
    <header class="name-band">
      <span class="owner-line">Kurt &amp;</span>
      <span class="owner-line">Melinda Ashcombe</span>
    </header>
    <div class="rule rule--gray-top"></div>
    <div class="rule rule--dark-top"></div>
    <section class="brand">
      <span class="brand-mark" aria-hidden="true"></span>
      <span class="brand-name">K&amp;M Hauling LLC</span>
    </section>
    <div class="rule rule--dark-bottom"></div>
    <div class="rule rule--gray-bottom"></div>
    <section class="contact-band">
      <p class="contact-line">
        <svg class="contact-icon" viewBox="0 0 20 24" aria-hidden="true"><rect x="4" y="2" width="12" height="20" rx="2" fill="none" stroke="#fff" stroke-width="2"/><rect x="7" y="5" width="6" height="9" fill="#fff"/></svg>
        402.618.2093 (Kurt)
      </p>
      <p class="contact-line">
        <svg class="contact-icon" viewBox="0 0 20 24" aria-hidden="true"><rect x="4" y="2" width="12" height="20" rx="2" fill="none" stroke="#fff" stroke-width="2"/><rect x="7" y="5" width="6" height="9" fill="#fff"/></svg>
        402.551.4387 (Melinda)
      </p>
      <p class="contact-line">
        <svg class="contact-icon" viewBox="0 0 20 24" aria-hidden="true"><rect x="1" y="7" width="18" height="13" fill="none" stroke="#fff" stroke-width="2"/><path d="M1 7 L10 14 L19 7" fill="none" stroke="#fff" stroke-width="2"/></svg>
        kmhaulingllc@mailora.net
      </p>
    </section>
  </article>
</main>
</body>
</html>
```